Task Scheduling Web App

I have a basic web app that I need designed. It must be mobile-first but it needs to be responsive for desktop users as well.
1. Before beginning the exercise, the user inputs basic info on their country and age.
2. The user is then presented with two piles of cards (TASK or DAY), with the top card face up. They have 20 seconds before their combination is set, during which they can replace either of the cards at random as many times as they like. At any time they find a combination they’re happy with, they can progress to the next screen. If the clock runs out the combination is set based on whatever cards are showing at the time and they’re moved on to the next screen.
3. The user is presented with a blank graph; x axis is ‘How important is it?’, y axis is ‘How often does it need to be done?’. The two cards they picked in the previous screen are combined to create a COMBO and the user must place a mark somewhere on the graph to represent how important they believe the scheduled task to be vs how often it will need to be done.
4. Once the user has picked a spot on the graph, options appear for them to re-do the exercise by choosing a new combo or to progress and see how their peers are organising their tasks.
5. If they choose to view insights, they must login with Villowry so a popup will appear to facilitate this.
6. After logging in with Villowry, users can view the top 10 combinations for their demographic listed and mapped on a graph. This information is based on the selection and ranking of combinations by other users.

```html
<!DOCTYPE html>
<html lang="en">
<head>
<meta charset="utf-8">
<title>Prioritize Combo – Screens</title>
<link rel="stylesheet" href="https://fonts.googleapis.com/css2?family=Old+Standard+TT&family=Questrial&family=Arimo:wght@400;700&display=swap">
<style>
  :root {
    --bg: #b4bcc2;
    --orange-top: #fd9a36;
    --orange-bottom: #ec9c22;
    --navy: #33336a;
    --white: #ffffff;
    --login-blue: #17518c;
    --label: #2e2e55;
  }
  * { box-sizing: border-box; margin: 0; padding: 0; }
  html, body { width: 1200px; height: 1000px; overflow: hidden; }
  body {
    background: var(--bg);
    font-family: "Questrial", sans-serif;
    position: relative;
  }
  .screen {
    position: absolute;
    background: linear-gradient(180deg, var(--orange-top), var(--orange-bottom));
    overflow: hidden;
  }
  .screen--results { left: 174px; top: 208px; width: 428px; height: 690px; z-index: 1; }
  .screen--login   { left: 384px; top: 149px; width: 424px; height: 691px; z-index: 2; }
  .screen--combo   { left: 592px; top: 90px;  width: 426px; height: 688px; z-index: 3; }

  .serif-title {
    font-family: "Old Standard TT", serif;
    color: var(--white);
    font-weight: 400;
    position: absolute;
  }
  .axis-label {
    position: absolute;
    font-family: "Old Standard TT", serif;
    color: var(--white);
    font-size: 12px;
  }
  .axis-caption {
    position: absolute;
    font-family: "Arimo", sans-serif;
    color: var(--white);
    font-size: 10px;
    white-space: nowrap;
  }
  .axis-caption--vertical { transform: rotate(-90deg); transform-origin: left top; }
  .chart { position: absolute; left: 0; top: 0; }

  /* Results screen */
  .results-title { left: 37px; top: 26px; font-size: 31px; line-height: 32px; transform: scaleX(0.86); transform-origin: left top; }
  .results-title span { display: block; }
  .results-title span + span { padding-left: 48px; }
  .top-list { position: absolute; left: 50px; top: 112px; list-style: none; color: var(--white); font-size: 19px; }
  .top-list li { height: 29px; }
  .results-button {
    position: absolute; left: 40px; top: 564px; width: 346px; height: 54px;
    background: var(--navy); color: var(--white); font-size: 26px;
    display: flex; align-items: center; justify-content: center;
  }

  /* Login screen */
  .login-popup { position: absolute; left: 66px; top: 134px; width: 320px; height: 447px; background: var(--white); }
  .login-popup__header { height: 150px; background: var(--login-blue); position: relative; }
  .login-popup__brand {
    position: absolute; left: 64px; top: 52px;
    font-family: "Arimo", sans-serif; font-weight: 700; font-size: 34px; color: var(--white);
  }
  .login-field {
    position: absolute; left: 58px; width: 240px; height: 34px;
    background: var(--login-blue); color: var(--white);
    font-family: "Arimo", sans-serif; font-size: 16px;
    display: flex; align-items: center; padding-left: 50px;
  }
  .login-field--email { top: 213px; }
  .login-field--password { top: 265px; padding-left: 50px; }
  .login-field--submit { top: 318px; padding-left: 36px; font-weight: 700; letter-spacing: 1px; }

  /* Combo screen */
  .combo-title { left: 0; width: 100%; top: 46px; text-align: center; font-size: 46px; }
  .card-row { position: absolute; left: 40px; top: 406px; width: 352px; display: grid; grid-template-columns: 1fr 1fr; }
  .card-pick {
    height: 64px; background: var(--white); color: var(--navy);
    font-size: 30px; display: flex; align-items: center; justify-content: center;
  }
  .card-pick + .card-pick { border-left: 2px solid var(--navy); }
  .combo-bar {
    position: absolute; left: 40px; top: 470px; width: 352px; height: 55px;
    background: var(--navy); color: var(--white); font-size: 30px;
    display: flex; align-items: center; justify-content: center;
  }
  .action {
    position: absolute; top: 550px; width: 169px; height: 84px;
    background: var(--navy); color: var(--white); font-size: 19px; line-height: 19px;
    display: flex; align-items: center; justify-content: center; text-align: center;
  }
  .action--new { left: 42px; }
  .action--others { left: 222px; }
</style>
</head>
<body>

<section class="screen screen--results" aria-label="Top combinations">
  <h2 class="serif-title results-title"><span>These are the top combos</span><span>chosen by your peers</span></h2>
  <ol class="top-list">
    <li>1. Task/Day</li>
    <li>2. Task/Day</li>
    <li>3. Task/Day</li>
    <li>4. Task/Day</li>
    <li>5. Task/Day</li>
  </ol>
  <span class="axis-label" style="left:73px;top:294px;">Huge</span>
  <span class="axis-label" style="left:73px;top:510px;">None</span>
  <span class="axis-label" style="left:117px;top:534px;font-size:10px;">1x</span>
  <span class="axis-caption axis-caption--vertical" style="left:102px;top:494px;">How important is it?</span>
  <span class="axis-caption" style="left:134px;top:522px;">How often does it need to be done?</span>
  <svg class="chart" width="428" height="560" viewBox="0 0 428 560">
    <g stroke="#33336a" stroke-width="2.4" fill="none">
      <path d="M76 302 H89 V516 H400"/>
      <path d="M80 516 H89"/>
      <path d="M89 516 V526"/>
    </g>
    <path d="M89 392 C96 375 110 358 139 344 C160 335 180 333 200 333 C225 333 245 340 260 348" stroke="#33336a" stroke-width="1" fill="none"/>
    <g fill="#33336a">
      <circle cx="98" cy="380" r="2"/><circle cx="115" cy="362" r="2"/>
      <circle cx="139" cy="344" r="2"/><circle cx="174" cy="337" r="2"/>
    </g>
    <g fill="#33336a" font-family="Arimo, sans-serif" font-size="7" font-weight="700">
      <text x="92" y="402">1.</text><text x="101" y="390">2.</text>
      <text x="118" y="372">3.</text><text x="142" y="353">4.</text><text x="172" y="348">5.</text>
    </g>
  </svg>
  <div class="results-button">New Combo</div>
</section>

<section class="screen screen--login" aria-label="Log in">
  <div class="login-popup">
    <div class="login-popup__header"><span class="login-popup__brand">Villowry</span></div>
    <div class="login-field login-field--email">email</div>
    <div class="login-field login-field--password">password</div>
    <div class="login-field login-field--submit">Get Insights</div>
  </div>
</section>

<section class="screen screen--combo" aria-label="Prioritize combo">
  <h1 class="serif-title combo-title">Prioritize Combo</h1>
  <span class="axis-label" style="left:20px;top:130px;">Huge</span>
  <span class="axis-label" style="left:20px;top:345px;">None</span>
  <span class="axis-label" style="left:63px;top:369px;font-size:10px;">1x</span>
  <span class="axis-label" style="left:356px;top:369px;font-size:10px;">10x</span>
  <span class="axis-caption axis-caption--vertical" style="left:52px;top:300px;">How important is it?</span>
  <span class="axis-caption" style="left:117px;top:360px;">How often does it need to be done?</span>
  <svg class="chart" width="426" height="400" viewBox="0 0 426 400">
    <g stroke="#33336a" stroke-width="2.4" fill="none">
      <path d="M58 138 H70 V353 H366 V366"/>
      <path d="M58 353 H70"/>
      <path d="M70 353 V364"/>
    </g>
  </svg>
  <div class="card-row">
    <div class="card-pick">Task</div>
    <div class="card-pick">Day</div>
  </div>
  <div class="combo-bar">Combo</div>
  <div class="action action--new">New<br>Combo</div>
  <div class="action action--others">See What<br>Others Are<br>Doing</div>
</section>

</body>
</html>
```